Flyer-Design für Vermietung und Verkauf von Palettenmöbeln
Zielgruppe
Ich vermiete und verkaufe in Tischler-Handarbeit hergestellte Palettenmöbel aus recycelten Paletten, wobei mein Schwerpunkt bei der Vermietung liegt. Meine Zielgruppe sind alle, die Veranstaltungen, Events , Messen, Präsentationen, private Feiern und Ähnliches planen und organisieren. Große und kleine Firmen, senatseigene Stellen, Privatpersonen, aber der Schwerpunkt liegt bei den Eventagenturen, welche mit der Organisation verschiedenster Veranstaltungen beauftragt werden.
Aufgabenstellung
Ich hätte ein klares und modernes Design mit BÄHM-Charakter. Der Flyer soll ein Hingucker sein, aber den Betrachter nicht erschlagen. Das Thema Nachhaltigkeit (die Möbel sind aus recylten Paletten) sollte bedacht werden. Ich hätte gern einen Faltflyer in DIN lang Größe. Dies ist für einen Mailing-Versand besser geeignet. Ich liefere eigene Bilder, aber sollten ein Stock-Bilder hilfreich sein, können dies gern verwendet werden. Ich habe natürlich noch mehr Bilder und kann diese gern zur Verfügung stellen, wenn ich weiß was benötigt wird. Es soll nicht viel Text in den Flyer. Ich bin hier sehr dankbar für Vorschläge, da ich mich mit dem Text sehr schwer tue. Ich hoffe, die Profis können mir auch beim Text helfen. Ich stelle auch Fotos meines alten Flyer zur Verfügung. Dieser ist definitv zu konservativ, langweilig und veraltet. Ich brauche ein modernes, hippes Design mit überzeugendem Text.

```html
<!DOCTYPE html>
<html lang="de">
<head>
<meta charset="utf-8">
<title>Kistenwerk – Palettenmöbel Faltflyer</title>
<link href="https://fonts.googleapis.com/css2?family=Montserrat:wght@300;400;500;600;700&display=swap" rel="stylesheet">
<style>
  :root {
    --green: #7cbc3e;
    --green-light: #8fc955;
    --green-dark: #5f9d2a;
    --ink: #4a4a4a;
    --ink-soft: #6b6b6b;
    --paper: #ffffff;
    --paper-grey: #f2f2f2;
    --stage: #e4e4e4;
    --wood: #c9a27a;
    --wood-dark: #8e6a48;
    --grass: #6fa83a;
  }
  * { box-sizing: border-box; margin: 0; padding: 0; }
  html, body { width: 1200px; height: 764px; overflow: hidden; }
  body {
    background: var(--stage);
    font-family: "Montserrat", Arial, sans-serif;
    color: var(--ink);
    position: relative;
  }
  .flyer {
    position: absolute;
    left: 135px; top: 52px;
    width: 930px; height: 660px;
    display: flex;
    box-shadow: 0 10px 30px rgba(0,0,0,.18);
  }
  .panel { position: relative; width: 310px; height: 660px; overflow: hidden; }

  /* Panel 1 – Über uns */
  .panel--about { background: var(--paper); }
  .about__box {
    position: absolute; left: 22px; top: 150px; width: 266px; height: 488px;
    background: var(--paper-grey);
  }
  .about__photo {
    position: absolute; left: 70px; top: 0; width: 240px; height: 210px;
    background: linear-gradient(160deg, #dcd3c7 0%, var(--wood) 45%, var(--wood-dark) 100%);
  }
  .about__tag {
    position: absolute; left: 30px; top: 168px; width: 120px; padding: 9px 12px;
    background: rgba(255,255,255,.92);
  }
  .about__tag strong { display: block; font-weight: 500; font-size: 15px; color: var(--ink); }
  .about__tag span { display: block; font-size: 10px; font-weight: 300; color: var(--ink-soft); }
  .about__tab {
    position: absolute; right: 0; top: 104px; width: 96px; height: 28px;
    background: var(--green); color: #fff; font-size: 9px; font-weight: 600;
    letter-spacing: 1px; display: flex; align-items: center; justify-content: center;
  }
  .about__rule { position: absolute; left: 42px; top: 210px; width: 1px; height: 420px; background: #bdbdbd; }
  .about__text { position: absolute; left: 60px; top: 245px; width: 225px; }
  .about__title { font-size: 16px; font-weight: 500; line-height: 1.3; margin-bottom: 14px; }
  .about__title em { font-style: normal; color: var(--green); }
  .about__text p { font-size: 9.5px; line-height: 1.55; color: var(--ink-soft); margin-bottom: 12px; }
  .about__text h3 { font-size: 10px; font-weight: 700; margin-bottom: 4px; }
  .about__claim { font-size: 10px; font-weight: 600; color: var(--green); line-height: 1.5; }

  /* Panel 2 – Kontakt */
  .panel--contact { background: #f6f6f6; }
  .contact__frame { position: absolute; inset: 26px 18px 26px 18px; border: 1px solid var(--green); }
  .contact__photo {
    position: absolute; left: 40px; top: 0; width: 270px; height: 190px;
    background: linear-gradient(180deg, #d9d9d9 0%, #c4c4c4 60%, #3a3a3a 100%);
  }
  .contact__name {
    position: absolute; left: 30px; top: 150px; width: 132px; padding: 8px 12px;
    background: var(--green); color: #fff;
  }
  .contact__name strong { display: block; font-weight: 400; font-size: 13px; }
  .contact__name span { display: block; font-size: 9px; font-weight: 300; }
  .brand {
    font-weight: 700; color: var(--green); font-size: 22px; letter-spacing: .5px;
    display: flex; align-items: center; gap: 8px;
  }
  .brand__mark { width: 12px; height: 12px; background: currentColor; }
  .contact__brand { position: absolute; top: 262px; left: 0; right: 0; display: flex; justify-content: center; }
  .contact__body { position: absolute; top: 330px; left: 0; right: 0; text-align: center; }
  .contact__body h2 { font-size: 15px; font-weight: 400; margin-bottom: 12px; }
  .contact__body h2 em { font-style: normal; color: var(--green); }
  .contact__intro { font-size: 9px; line-height: 1.6; color: var(--ink-soft); margin-bottom: 16px; }
  .contact__address { font-size: 9.5px; line-height: 1.6; color: var(--ink-soft); font-style: normal; margin-bottom: 16px; }
  .contact__address strong { display: block; font-size: 12px; color: var(--ink); font-weight: 600; }
  .contact__web { font-size: 10px; font-weight: 700; color: var(--green); }

  /* Panel 3 – Titel */
  .panel--cover { background: var(--paper); }
  .cover__photo {
    position: absolute; inset: 0;
    background: linear-gradient(180deg, #eeeeee 0%, #dcd0c2 30%, var(--wood) 55%, #a8865f 68%, var(--grass) 80%, #5b922e 100%);
  }
  .cover__band {
    position: absolute; left: 0; top: 0; width: 310px; height: 150px; background: var(--green);
    color: #fff; padding: 50px 22px 0;
  }
  .cover__band h1 { font-size: 24px; font-weight: 600; letter-spacing: 1px; }
  .cover__band p { font-size: 14px; font-weight: 400; margin-top: 2px; }
  .cover__frame { position: absolute; inset: 34px 14px 26px 14px; border: 1px solid rgba(255,255,255,.85); }
  .cover__brand { position: absolute; top: 230px; left: 0; right: 0; display: flex; justify-content: center; }
  .cover__brand .brand { color: #fff; font-size: 28px; }
  .cover__claim {
    position: absolute; left: 14px; bottom: 78px; width: 230px; padding: 14px 16px;
    background: rgba(255,255,255,.82);
  }
  .cover__claim h2 { font-size: 19px; font-weight: 500; line-height: 1.2; }
  .cover__claim p { font-size: 11px; margin-top: 6px; color: var(--ink-soft); }
</style>
</head>
<body>
  <main class="flyer">
    <section class="panel panel--about">
      <div class="about__box"></div>
      <div class="about__photo" role="img" aria-label="Foto: Palettenmöbel mit Stehtischen und Weinflaschen auf einer Veranstaltung"></div>
      <div class="about__tag"><strong>Vielfältig</strong><span>einsetzbar</span></div>
      <div class="about__tab">ÜBER UNS</div>
      <div class="about__rule"></div>
      <div class="about__text">
        <h2 class="about__title">Wir verkaufen <em>&amp;</em> vermieten hochwertige handgefertigte Möbel aus Europaletten</h2>
        <p>Machen Sie Ihr Firmenevent oder Ihre private Feier zu einem Erlebnis mit hochwertigen handgefertigten Palettenmöbeln.</p>
        <h3>Der Umwelt zuliebe</h3>
        <p>In einer Welt, in der Nachhaltigkeit eine immer größere Rolle spielt, erhalten Sie bei uns Möbel aus recycelten Europaletten.</p>
        <p class="about__claim">Wir vermieten und liefern in Berlin und Umgebung.</p>
      </div>
    </section>

    <section class="panel panel--contact">
      <div class="contact__frame"></div>
      <div class="contact__photo" role="img" aria-label="Porträtfoto der Inhaberin"></div>
      <div class="contact__name"><strong>Ilka Brandner</strong><span>Inhaberin</span></div>
      <div class="contact__brand"><div class="brand"><span class="brand__mark"></span>Kistenwerk</div></div>
      <div class="contact__body">
        <h2>Sie haben Fragen<em>?</em></h2>
        <p class="contact__intro">Wir beraten Sie gerne!<br>Für mehr Informationen besuchen<br>Sie uns gerne auch online.</p>
        <address class="contact__address">
          <strong>Ilka Brandner</strong>
          Lindenweg 14<br>13599 Berlin<br><br>
          T. +49 (0) 170 5550182<br>E. info@kistenwerk-moebel.de
        </address>
        <p class="contact__web">www.kistenwerk-moebel.de</p>
      </div>
    </section>

    <section class="panel panel--cover">
      <div class="cover__photo" role="img" aria-label="Foto: Sitzgruppe aus Palettenmöbeln auf Kunstrasen vor heller Ziegelwand"></div>
      <div class="cover__band">
        <h1>PALETTENMÖBEL</h1>
        <p>aus recycelten Paletten</p>
      </div>
      <div class="cover__frame"></div>
      <div class="cover__brand"><div class="brand"><span class="brand__mark"></span>Kistenwerk</div></div>
      <div class="cover__claim">
        <h2>Nachhaltig mieten oder kaufen</h2>
        <p>in Berlin und Umgebung</p>
      </div>
    </section>
  </main>
</body>
</html>
```